Bloom Where You Stand redesign book cover

A new cover for my already published book. The old cover looks great but not for a women’s self help book. Cover is killing sales. Once I explain the book it sells quickly AND gets 5 star reviews. Outside of actually explaining the book the cover scares people away. I need a new cover. ASAP! Before The yr end please.
The tag line -
Discover 10 Practical Ways To Replace negative thoughts with knowing the voice of God. This is a self help book for women 35-45 Christian but not religious. Each chapter is a hands on spiritual experience where the reader takes small tests about themselves, discover why they have negative thoughts, what they are and how to listen to God through hands on methods of listening. NOT strange type of things. They learn what 4 voices they are listening to and how to hone in on Jesus voice. There are scriptures to pray and journaling assignments. The old cover is in the brief with the write up for the back of the book. Please use the new author picture, Publishers logo (tree), barcode, and contact info from the back of the book. And yes the author name and title of the book on the spine. Lay out on the back cover needs to be interesting. You have all the info have fun with it.

Target Market(s)

Women 35-45 yrs old Christian and new believers or seekers.

Industry/Entity Type

Non profit organization. Missionary

Requirements
Must have
• Something DIFFERENT than what is there now. Something inviting. Fresh clear title
Nice to have
• Multi colors however a white stand out cover is also good.
Should not have
• Heavy religious feeling. No church steeples, Jesus faces.

```html
<!DOCTYPE html>
<html lang="en">
<head>
<meta charset="UTF-8">
<title>Bloom Where You Stand — Book Cover</title>
<link href="https://fonts.googleapis.com/css2?family=Bebas+Neue&family=Montserrat:wght@700;800&display=swap" rel="stylesheet">
<style>
  :root {
    --teal: #127a6b;
    --mustard: #eaa814;
    --orange: #f7a63c;
    --white: #ffffff;
    --soft-white: #f1ecec;
    --photo-dark: #2f2f2f;
    --photo-mid: #6f6f6f;
    --photo-light: #a8a8a8;
  }
  * { margin: 0; padding: 0; box-sizing: border-box; }
  html, body { width: 848px; height: 1200px; overflow: hidden; background: #fff; }
  .cover {
    position: relative;
    width: 848px;
    height: 1200px;
    overflow: hidden;
    background: var(--photo-mid);
  }
  .cover-art { position: absolute; inset: 0; }
  .ghost-word {
    position: absolute;
    font-family: "Montserrat", sans-serif;
    font-weight: 800;
    color: rgba(255,255,255,0.13);
    line-height: 1;
    letter-spacing: -10px;
    white-space: nowrap;
  }
  .ghost-word--top { left: -40px; top: -20px; font-size: 470px; }
  .ghost-word--bottom { left: -120px; top: 820px; font-size: 520px; }
  .title {
    position: absolute;
    left: 70px;
    top: 92px;
    font-family: "Bebas Neue", sans-serif;
    font-weight: 400;
    color: var(--white);
    font-size: 228px;
    line-height: 217px;
    letter-spacing: 1px;
    text-shadow: 0 8px 22px rgba(0,0,0,0.35);
  }
  .title span { display: block; white-space: nowrap; }
  .title .title-last { font-size: 196px; }
  .tagline {
    position: absolute;
    left: 64px;
    top: 766px;
    width: 720px;
    font-family: "Montserrat", sans-serif;
    font-weight: 700;
    font-size: 24.5px;
    line-height: 32px;
    letter-spacing: -0.4px;
    color: var(--soft-white);
  }
  .tagline .highlight { color: var(--orange); }
  .author {
    position: absolute;
    left: 322px;
    top: 1125px;
    font-family: "Montserrat", sans-serif;
    font-weight: 800;
    font-size: 33px;
    color: var(--white);
    letter-spacing: -0.5px;
  }
</style>
</head>
<body>
<main class="cover">
  <svg class="cover-art" width="848" height="1200" viewBox="0 0 848 1200" xmlns="http://www.w3.org/2000/svg">
    <defs>
      <linearGradient id="photoTone" x1="0" y1="0" x2="0.4" y2="1">
        <stop offset="0" stop-color="var(--photo-dark)"/>
        <stop offset="0.45" stop-color="var(--photo-mid)"/>
        <stop offset="1" stop-color="var(--photo-light)"/>
      </linearGradient>
    </defs>
    <rect class="portrait-photo" width="848" height="1200" fill="url(#photoTone)" role="img" aria-label="Black and white close-up photograph of a woman's lower face"/>
    <rect class="mustard-block" x="0" y="0" width="230" height="300" fill="var(--mustard)"/>
    <path class="teal-shape" d="M0 0 H228 C240 240 360 420 470 640 C520 750 510 880 400 980 C300 1070 140 1105 0 1118 Z" fill="var(--teal)"/>
    <rect class="mustard-block" x="0" y="0" width="228" height="230" fill="var(--mustard)"/>
  </svg>

  <div class="ghost-word ghost-word--top" aria-hidden="true">OUT</div>
  <div class="ghost-word ghost-word--bottom" aria-hidden="true">OUT</div>

  <h1 class="title">
    <span>Bloom</span>
    <span>Where</span>
    <span class="title-last">You Stand</span>
  </h1>

  <p class="tagline">Discover 10 Practical Ways To Replace negative thoughts with knowing the <span class="highlight">voice of God.</span></p>

  <p class="author">Lena Hartwell</p>
</main>
</body>
</html>
```